Byteloft - Your IT support team - online sales website design concept

Byteloft aims to provide home and small business users with high quality, friendly and affordable IT support.

We are delivering this service through the website. Users will choose a support service that they want, enter some details, make a payment and then be connected to our support team member who will resolve their problem and discuss their IT with them by remotely controlling their computer and speaking to them on the phone.

This design project is to develop the website design concept which will:

# Give the user confidence that byteloft are a legitimate business giving premium yet good value IT support.
# Inform the users of our IT services.
# Encourage the user to try our services.
# Look fun, interesting, modern, respectable and trustworthy.

We intend to offer 4 core 'products' to our users, these are:
# Virus removal – We will clean your PC then protect it for the future
# Computer Speed Up – Optimise you PC to get the most out of it
# Skyvault your IT- auto backup of PC with remote access to documents, pictures, videos and email
# IT Support – to fix a problem or we can just help out

We are open to any fun or interesting ways of getting this message across to users.

We have the following idea which could be useful but does not have to be used in design concepts:

Perhaps a home/detached house on the front page with a cloud in the sky for our cloud service, a fast car on the drive or something to demonstrate computer speed up, a gremlin in the drain for virus removal and our byteloft yellow waves from our logo emanating towards the house as our general IT support offering. Maybe having some movement or information on mouse over.

We like the idea of real life images embedded into the page similar to this:

http://www.prolivasad.cz/

But, ideas could be cartoon based or whatever you think will look good. Any interesting concepts are welcome.

We want to have our 4 'products' clearly displayed on the home page. They could be in 4 boxes beneath some nice image or incorporated into a single nice image/cartoon or graphic. If incorporated into one graphic/cartoon/image we would have clickable areas of the image.

We want it to be clear to visitors what it is we are offering - IT support to remotely solve a computer/iPad/smartphone issue and that we are "Online now to fix your problem".

We might also want to feature 4 features/benefits:

UK Based Engineers (with GB flag)
Remote IT Support
Premium Support
Money Back Guarantee

We have a logo already which is attached. We would like a homepage design encompassing the features set out above, a second page design to be used as the main page when you click on one of the 4 'products' and also a general content page design so that we have a theme for the site. We just want these designs as images for this project.

Thank you for your interest.

Reason: 10 days was never long enough and we needed more time to respond to designers.

Reason: I've been away on holiday and I want some more time to respond to designers. Thanks, Colin

Target Market(s)

Home and small business users.

Industry/Entity Type

Small Business

Requirements
Must have
• We would like an area, to show whether we are open and online or not. When staff are available to deliver remote support the site should clearly show that staff are online working and available now to support. When we are offline the site should also show this.

We will offer our users a "Money Back Guarantee"; if they are not happy with the work that we do for them we will refund them.

```html
<!DOCTYPE html>
<html lang="en">
<head>
<meta charset="utf-8">
<title>Byteloft – Your IT support team</title>
<link href="https://fonts.googleapis.com/css2?family=Raleway:wght@300;400;500;600;700&family=Open+Sans:wght@400;700&display=swap" rel="stylesheet">
<style>
  :root{
    --yellow:#f6c21a;
    --ink:#1d1d1b;
    --cream-top:#fffdf6;
    --cream-bottom:#f7eccb;
    --teal-sky:#9fd3d3;
    --teal:#2f8a86;
    --green:#6aab1e;
    --blue:#1f8fd6;
    --orange:#e8650f;
    --blob:#eaf4f3;
    --text-grey:#9a9a9a;
    --link-blue:#3a9fc7;
    --panel:#efefef;
    --footer:#e7e8e4;
    --footer-text:#6d6d6d;
  }
  *{box-sizing:border-box;margin:0;padding:0}
  html,body{width:1004px;height:1200px;overflow:hidden;background:#fff}
  body{position:relative;font-family:"Raleway",sans-serif;color:var(--ink)}

  .site-header{position:absolute;left:0;top:0;width:1004px;height:96px;
    background:linear-gradient(var(--cream-top),var(--cream-bottom))}
  .brand-name{position:absolute;left:117px;top:12px;font-family:"Raleway",sans-serif;
    font-weight:700;font-size:50px;letter-spacing:-1px;color:var(--ink);line-height:1}
  .brand-tagline{position:absolute;left:148px;top:73px;font-family:"Open Sans",sans-serif;
    font-size:13px;color:#333}
  .header-social{position:absolute;left:716px;top:31px;display:flex;gap:4px}
  .header-social span{width:33px;height:33px;border-radius:50%;display:block;
    background:radial-gradient(circle at 40% 35%,#d9e4ee,#6d8aa8);border:2px solid #fff;box-shadow:0 1px 2px rgba(0,0,0,.3)}

  .main-nav{position:absolute;left:0;top:96px;width:1004px;height:31px;background:var(--ink);
    border-bottom:3px solid var(--yellow)}
  .main-nav a{position:absolute;top:0;height:31px;line-height:31px;color:#fff;text-decoration:none;
    font-family:"Open Sans",sans-serif;font-weight:700;font-size:16px}
  .main-nav a.active{background:var(--yellow);color:var(--ink);padding:0 7px}

  .hero{position:absolute;left:0;top:129px;width:1004px;height:410px}
  .hero svg{position:absolute;left:0;top:0}
  .product{position:absolute;top:22px;width:185px}
  .product h2{font-family:"Raleway",sans-serif;font-weight:600;font-size:14.5px;line-height:18px;color:var(--ink)}
  .product p{font-size:11.5px;line-height:15px;color:var(--ink);margin-top:4px}

  .welcome{position:absolute;left:117px;top:552px;width:470px}
  .welcome h1{font-weight:600;font-size:30px;line-height:38px}
  .welcome h1 .accent{color:var(--yellow)}
  .welcome p{margin-top:6px;font-size:11.5px;line-height:17.6px;color:var(--text-grey)}

  .services{position:absolute;left:117px;top:760px;width:470px}
  .services h2{font-weight:400;font-size:20px;line-height:26px}
  .services ul{list-style:none;position:absolute;top:35px;width:220px}
  .services ul.col-2{left:232px}
  .services li{height:23.3px;font-size:11.5px;color:var(--link-blue);padding-left:16px;position:relative;font-weight:500}
  .services li::before{content:"›";position:absolute;left:4px;top:-3px;color:#b5b5b5;font-size:14px}

  .sidebar{position:absolute;left:617px;top:545px;width:262px;height:490px;background:var(--panel)}
  .sidebar h3{position:absolute;font-weight:600;font-size:19px;line-height:20px}
  .sidebar h3 span{display:block;font-weight:400;font-size:20px}
  .why-text{position:absolute;left:12px;top:62px;width:236px;font-size:11.5px;line-height:18px;color:#555}
  .learn-more{position:absolute;left:12px;top:214px;font-size:10px;font-weight:700;color:var(--link-blue);letter-spacing:.3px}
  .sidebar hr{position:absolute;left:10px;top:242px;width:240px;border:0;border-top:2px solid #ddd}
  .quote-mark{position:absolute;left:10px;top:298px;font-family:"Open Sans",sans-serif;font-size:90px;line-height:1;color:#d3d3d3;font-weight:700}
  .testimonial{position:absolute;left:58px;top:310px;width:190px;font-size:11.5px;line-height:18px;color:#555}
  .testimonial-author{position:absolute;left:57px;top:457px;font-size:11.5px;font-weight:500;color:var(--ink)}

  .site-footer{position:absolute;left:0;top:1060px;width:1004px;height:140px;background:var(--footer);border-top:1px solid #d6d6d2}
  .footer-nav{position:absolute;left:117px;top:20px;display:flex;gap:19px;font-size:12px;color:var(--footer-text)}
  .newsletter{position:absolute;left:606px;top:18px;display:flex;align-items:center;gap:7px}
  .newsletter label{font-family:"Raleway",sans-serif;font-weight:600;font-size:13px;color:var(--ink)}
  .newsletter .field{width:188px;height:25px;background:#fff;border:1px solid #c9c9c9;border-radius:3px;position:relative;
    font-size:10px;color:#555;line-height:23px;padding-left:8px}
  .newsletter .send{position:absolute;right:2px;top:2px;width:21px;height:19px;background:#1e2a38;border-radius:2px}
  .footer-social{position:absolute;left:437px;top:55px;display:flex;gap:6px}
  .footer-social span{width:36px;height:36px;border-radius:50%;border:2px solid #c4c4c4;background:#f1f1ef;display:block}
  .copyright{position:absolute;left:0;width:1004px;top:103px;text-align:center;font-size:10.5px;color:#444}
</style>
</head>
<body>

<header class="site-header">
  <div class="brand-name">byteloft</div>
  <div class="brand-tagline">your IT support team</div>
  <div class="header-social" aria-label="Social links"><span></span><span></span><span></span></div>
</header>

<nav class="main-nav">
  <a class="active" href="#" style="left:143px">HOME</a>
  <a href="#" style="left:244px">ABOUT</a>
  <a href="#" style="left:342px">SERVICES</a>
  <a href="#" style="left:464px">WORK</a>
  <a href="#" style="left:555px">BLOG</a>
  <a href="#" style="left:644px">CAREERS</a>
  <a href="#" style="left:767px">CONTACT</a>
</nav>

<section class="hero">
  <svg width="1004" height="410" viewBox="0 0 1004 410">
    <rect width="1004" height="410" fill="var(--teal-sky)"/>
    <!-- product tails -->
    <path d="M112,32 C92,55 98,85 118,98" fill="none" stroke="var(--teal)" stroke-width="2"/>
    <path d="M307,32 C292,60 300,95 345,100" fill="none" stroke="var(--green)" stroke-width="2"/>
    <path d="M502,32 C484,70 494,110 545,130" fill="none" stroke="var(--blue)" stroke-width="2"/>
    <path d="M695,32 C680,55 688,75 705,80" fill="none" stroke="var(--orange)" stroke-width="2"/>
    <!-- product blobs -->
    <path d="M150,78 C235,68 305,160 322,240 C335,305 262,336 170,336 C88,336 60,290 64,220 C70,150 100,84 150,78Z" fill="var(--blob)" stroke="var(--teal)" stroke-width="4"/>
    <path d="M360,95 C430,85 490,170 500,240 C508,300 470,335 400,333 C320,330 262,285 264,225 C266,160 305,100 360,95Z" fill="var(--blob)" stroke="var(--green)" stroke-width="4"/>
    <path d="M570,128 C640,118 700,200 706,268 C710,330 665,362 600,360 C520,356 468,310 470,250 C472,185 515,133 570,128Z" fill="var(--blob)" stroke="var(--blue)" stroke-width="4"/>
    <path d="M800,62 C850,58 876,120 875,190 C874,255 835,288 770,285 C700,282 655,240 657,185 C660,120 740,66 800,62Z" fill="var(--blob)" stroke="var(--orange)" stroke-width="4"/>
    <!-- illustration areas -->
    <circle cx="175" cy="208" r="75" fill="#d8e7df" role="img" aria-label="Illustration of a virus crossed out in a red prohibition sign"/>
    <rect x="300" y="150" width="160" height="140" rx="20" fill="#c9d2d4" role="img" aria-label="Illustration of a computer tower on wheels speeding along"/>
    <ellipse cx="590" cy="255" rx="68" ry="70" fill="#bcdaf0" role="img" aria-label="Illustration of a blue cloud carrying folders of documents and photos"/>
    <rect x="705" y="105" width="135" height="145" rx="18" fill="#f2d7df" role="img" aria-label="Illustration of speech bubbles with question marks above a support monitor"/>
    <!-- sweeping bands -->
    <path d="M0,365 C300,415 700,400 1004,292 L1004,345 C760,420 400,430 0,372Z" fill="var(--yellow)"/>
    <path d="M0,362 C300,412 700,396 1004,290 L1004,318 C760,400 400,420 0,368Z" fill="var(--ink)"/>
    <path d="M0,375 C400,435 760,425 1004,345 L1004,410 L0,410Z" fill="#fff"/>
  </svg>
  <div class="product" style="left:117px"><h2>VIRUS REMOVAL</h2><p>We will clean your PC then protect it for the future</p></div>
  <div class="product" style="left:311px"><h2>COMPUTER SPEED UP</h2><p>Optimise you PC to get the most out of it</p></div>
  <div class="product" style="left:505px;width:180px"><h2>SKYVAULT YOUR IT</h2><p>auto backup of PC with remote access to documents, pictures, videos and email</p></div>
  <div class="product" style="left:698px"><h2>IT SUPPORT</h2><p>to fix a problem or we can just help out</p></div>
</section>

<section class="welcome">
  <h1>Welcome to <span class="accent">byte</span>loft</h1>
  <p>Lorem Ipsum is simply dummy text of the printing and typesetting industry. Lorem Ipsum has been the industry's standard dummy text ever since the 1500s, when an unknown printer took a galley of type and scrambled it to make a type specimen book. It has survived not only five centuries, but also the leap into electronic typesetting, remaining essentially unchanged. It was popularised in the 1960s with the release of Typeplate sheets containing Lorem Ipsum passages, and more recently with desktop publishing software like Folio Layout including versions of Lorem Ipsum.</p>
</section>

<section class="services">
  <h2>Our Services</h2>
  <ul class="col-1">
    <li>Lorem ipsum dolor sit amet</li>
    <li>consectetur adipiscing elit</li>
    <li>Nullam auctor sem accumsan</li>
    <li>semper metus et, pharetra nunc</li>
    <li>Lorem ipsum dolor sit amet</li>
    <li>consectetur adipiscing elit</li>
    <li>Nullam auctor sem accumsan</li>
  </ul>
  <ul class="col-2">
    <li>Lorem ipsum dolor sit amet</li>
    <li>consectetur adipiscing elit</li>
    <li>Nullam auctor sem accumsan</li>
    <li>semper metus et, pharetra nunc</li>
    <li>Lorem ipsum dolor sit amet</li>
    <li>consectetur adipiscing elit</li>
    <li>Nullam auctor sem accumsan</li>
  </ul>
</section>

<aside class="sidebar">
  <h3 style="left:15px;top:12px">Why<span>byteloft</span></h3>
  <p class="why-text">NimbusLine Mobile business telephone service makes every business better: more professional, more efficient and more profitable. We help our customers grow their businesses through easy-to-use features that improve productivity and give the business a professional telephone presence.</p>
  <div class="learn-more">LEARN MORE</div>
  <hr>
  <h3 style="left:11px;top:260px">Customer<span>Say</span></h3>
  <div class="quote-mark">“</div>
  <p class="testimonial">Lorem ipsum dolor sit amet, consectetur adipiscing elit, sed do eiusmod tempor incididunt ut labore et dolore magna aliqua. Ut enim ad minim veniam, quis nostrud exercitation ullamco laboris nisi ut aliquip ex ea commodo.</p>
  <div class="testimonial-author">John Doe, Some Business</div>
</aside>

<footer class="site-footer">
  <div class="footer-nav"><span>Home</span><span>About</span><span>Services</span><span>Work</span><span>Blog</span><span>Careers</span><span>Contact</span></div>
  <div class="newsletter">
    <label>NEWSLETTER</label>
    <div class="field">Enter your email address
      <span class="send"><svg width="21" height="19" viewBox="0 0 21 19"><rect x="5" y="5" width="11" height="8" fill="#fff"/><path d="M5,5 L10.5,10 L16,5" fill="none" stroke="#1e2a38" stroke-width="1"/></svg></span>
    </div>
  </div>
  <div class="footer-social" aria-label="Social links"><span></span><span></span><span></span></div>
  <div class="copyright">© 2013 byteloft. All rights reserved.</div>
</footer>

</body>
</html>
```